Concise,Good colour matching,Good looks design for "HERD SURE RAPID TEST FOR LIVESTOCK"

Product Positioning: Affordable test for Large Animals (Livestock/Veterinary Use)
Product Name: HERD SURE Rapid Test Kit (for large animals, e.g., cattle, horses, swine,Avian,sheep).

2. Packaging Requirements

A. Visual Design
Color Scheme:
Green/Blue/Orange/Yellow/Red/Gray/White(chose 2~4 colors)

Mandatory Info:
Brand logo ("HERD SURE")

Target Market(s)

Southeast Asia, Africa, Middle East, South America

Industry/Entity Type

Veterinary diagnostic for LIVESTOCK

Colors

Designer to choose colors to be used in the design.

Requirements
Nice to have
• Concise,Good colour matching,Good looks

```html
<!DOCTYPE html>
<html lang="en">
<head>
<meta charset="utf-8">
<title>HERD SURE Rapid Test – Box Dieline</title>
<link rel="stylesheet" href="https://fonts.googleapis.com/css2?family=Anton&family=Archivo:wght@400;700&display=swap">
<style>
  :root {
    --brand-blue: #36a8df;
    --title-blue: #2b93d3;
    --panel-light: #9dd3f0;
    --accent-orange: #f39200;
    --photo-deep: #3a84b6;
    --photo-mid: #5ea7d6;
    --photo-light: #86c6ea;
    --white: #ffffff;
    --page: #ffffff;
  }
  * { margin: 0; padding: 0; box-sizing: border-box; }
  html, body {
    width: 716px; height: 1200px; overflow: hidden;
    background: var(--page);
  }
  .canvas { position: relative; width: 716px; height: 1200px; }

  .dieline { position: absolute; left: 36px; top: 325px; width: 643px; height: 549px; }

  .panel { position: absolute; overflow: hidden; }

  /* Top lid panel */
  .panel--lid { left: 0; top: 0; width: 418px; height: 307px; background: var(--brand-blue); }
  .panel--side { left: 419px; top: 0; width: 224px; height: 307px; background: var(--brand-blue); }
  .panel--front { left: 0; top: 308px; width: 418px; height: 241px; background: var(--brand-blue); }

  .livestock-photo {
    position: absolute; left: 0; top: 0; width: 100%; height: 219px;
    background: linear-gradient(90deg, var(--photo-deep) 0%, var(--photo-mid) 35%, var(--photo-light) 60%, var(--photo-mid) 80%, var(--photo-deep) 100%);
  }
  .info-field {
    position: absolute; left: 0; top: 0; width: 100%; height: 219px;
    background: var(--panel-light);
  }

  .tagline-band {
    position: absolute; left: 0; width: 100%; height: 22px;
    background: var(--accent-orange);
  }
  .panel--lid .tagline-band, .panel--side .tagline-band { top: 219px; }
  .panel--front .tagline-band { top: 137px; }

  .tagline {
    position: absolute; left: 51px; top: 0; line-height: 22px;
    font-family: "Archivo", Arial, sans-serif; font-weight: 700;
    font-size: 11.6px; letter-spacing: 0.3px; color: var(--white);
    white-space: nowrap;
  }

  .brand-name {
    position: absolute; right: 37px;
    font-family: "Anton", "Oswald", sans-serif; font-size: 41px; line-height: 1;
    color: var(--white); letter-spacing: 0.5px; white-space: nowrap;
  }
  .panel--lid .brand-name { top: 246px; }
  .panel--front .brand-name { top: 164px; }

  /* Rotated product copy on the side flap */
  .product-copy {
    position: absolute; left: 40px; top: 192px; width: 165px; height: 145px;
    transform-origin: 0 0; transform: rotate(-90deg);
    font-family: "Archivo", Arial, sans-serif; color: var(--white);
  }
  .product-copy__title {
    font-family: "Anton", "Oswald", sans-serif; font-weight: 400;
    font-size: 13.5px; color: var(--title-blue); letter-spacing: 0.2px;
    margin-bottom: 8px; white-space: nowrap;
  }
  .feature { margin-bottom: 9px; }
  .feature__heading { font-size: 8px; font-weight: 700; color: var(--title-blue); line-height: 1.15; }
  .feature__text { font-size: 6.2px; line-height: 1.3; color: var(--white); white-space: nowrap; }
</style>
</head>
<body>
<main class="canvas">
  <div class="dieline">

    <section class="panel panel--lid">
      <div class="livestock-photo" role="img" aria-label="Blue duotone vertical strips showing horses, chickens and a river landscape"></div>
      <div class="tagline-band"><span class="tagline">AFFORDABLE DIAGNOSTICS FOR HEALTHY HERDS</span></div>
      <h1 class="brand-name">HERD SURE</h1>
    </section>

    <section class="panel panel--side">
      <div class="info-field"></div>
      <div class="product-copy">
        <h2 class="product-copy__title">HERD SURE RAPID TEST</h2>
        <div class="feature">
          <h3 class="feature__heading">Fast &amp; Efficient:</h3>
          <p class="feature__text">Rapid test results in less than 10 minutes<br>from prep to completion.</p>
        </div>
        <div class="feature">
          <h3 class="feature__heading">Affordable:</h3>
          <p class="feature__text">"Colloidal gold-based rapid tests that combine<br>high accuracy with cost-effectiveness."</p>
        </div>
        <div class="feature">
          <h3 class="feature__heading">Reliable &amp; Simple:</h3>
          <p class="feature__text">Stable test performance with 2~30°C,<br>Easy to operate, no professional skills required.</p>
        </div>
      </div>
      <div class="tagline-band"></div>
    </section>

    <section class="panel panel--front">
      <div class="tagline-band"><span class="tagline">AFFORDABLE DIAGNOSTICS FOR HEALTHY HERDS</span></div>
      <p class="brand-name">HERD SURE</p>
    </section>

  </div>
</main>
</body>
</html>
```